Verdant Row

Currently www.verdantrow-example.com. This site was designed with a generic templet. However it is functional. I'm looking for a fun, fresh, and professional design. I also need help getting the XML for Searchly and Findo. I'm not a web designer and need help. I do not like my current sites narrow width.
Updates

All and all I'm liking the designs. The earlier ones seem better. Some seem that they are just taking my images and inputing them into a templet. I could have done that. The pictures are nice. Please keep in mind, functionality and updates. Please help us show our customers our how we are different. Safe Reliable Responsible are the key fundamentals, inside of these fundamentals show that were are customer service specialized. We are, Licensed, Insured, Drug Screened, Criminally Screened. Seems that people are putting up nice pictures but not capturing our values. Please help us market us on our website. Show our prospective customers why we are better, how we differentiate ourself from the competitors. Why choose us? Our flyers and cards are designed to drive our prospective customers to the website. If it looks identical with no pazaz like the card, then the marketing chain failed. I included our cards to help guide the thought process of our company. The link below is a feature I would love to have. This may be another project itself. I'm not sure if PX is the place to accomplish it. Below is a link for people to estimate there lawns with globe viewer. I would like to give a range of estimates using this technology. I have no clue how to accomplish it. If anyone knows how to who could do this, Please let me know. https://www.yardquoter-example.com/showOrder/MOWLAWN/propertyDetails

Target Market(s)

We target residential customers 30-80 yr old. We also are expanding and placing a special emphasis on Business accounts. The main service is a mowing and landscape maintenance. Should be the main focus of the site.

Industry/Entity Type

Searchly

Coding

Coded - Design and coding required

Font styles to use
Sans Serif

Requirements
Must have
• I want this site to be fun and colorful. It still needs to be professional looking as not to deter business accounts. If you use photos, they must reflect Florida lawn. Note the architecture the homes, grass type, types of plants.
Should not have
• My current site is ok. I use it just as a

```html
<!DOCTYPE html>
<html lang="en">
<head>
<meta charset="utf-8">
<title>Verdant Row – Lawn Care</title>
<link href="https://fonts.googleapis.com/css2?family=Arimo:ital,wght@0,400;0,700;1,700&display=swap" rel="stylesheet">
<style>
:root{
  --sky-top:#4fb3ea;
  --sky-low:#bfe3f7;
  --grass-light:#7dc043;
  --grass:#5c9e2c;
  --intro-bg:#5a9a2b;
  --services-bg:#4b8b22;
  --accent-lime:#b6f06a;
  --cta-red:#d7372a;
  --cta-red-dark:#a8261c;
  --mascot-red:#e2402c;
  --soil:#3d2b12;
  --soil-deep:#2b1d0a;
  --footer:#151515;
  --nav-dark:#37474f;
  --white:#ffffff;
  --ink:#111111;
}
*{margin:0;padding:0;box-sizing:border-box}
html,body{width:786px;height:1200px;overflow:hidden}
body{font-family:"Arimo",Arial,sans-serif;color:var(--white);position:relative;background:var(--footer)}

.hero{position:absolute;left:0;top:0;width:786px;height:372px;overflow:hidden}
.hero-scene{position:absolute;inset:0;background:linear-gradient(180deg,var(--sky-top) 0%,var(--sky-low) 38%,var(--grass-light) 56%,var(--grass) 100%)}
.mascot{position:absolute;left:494px;top:168px;width:228px;height:150px;border-radius:46px 46px 28px 28px;background:linear-gradient(180deg,var(--mascot-red),#c42f20)}

.brand{position:absolute;left:56px;top:26px;display:flex;align-items:center;gap:6px;font-weight:700;font-size:17px;color:#1f5d12}
.brand-dot{width:11px;height:11px;border-radius:50%;background:var(--cta-red)}
.service-area{position:absolute;right:53px;top:15px;font-size:11px;color:var(--white)}
.call{position:absolute;right:53px;top:30px;font-size:15px;color:var(--white)}
.call strong{font-size:20px;font-weight:700}

.nav{position:absolute;left:52px;top:56px;width:682px;height:25px;display:flex;background:var(--white)}
.nav a{flex:1;font-size:9px;color:#333;text-decoration:none;display:flex;align-items:center;justify-content:center;border-right:1px solid #ccc}
.nav a.is-active{background:var(--cta-red);color:var(--white);flex:0 0 81px}
.nav a.portal{background:var(--nav-dark);color:var(--white);border:0;flex:0 0 121px;gap:8px}
.nav a.portal svg{width:12px;height:12px}

.tagline{position:absolute;left:53px;top:112px;color:var(--ink)}
.tagline p{font-size:21px}
.tagline h1{font-size:34px;font-style:italic;font-weight:700;line-height:41px;margin-top:6px;text-transform:uppercase}
.btn-quote{position:absolute;display:flex;align-items:center;justify-content:center;background:var(--cta-red);border:2px solid var(--cta-red-dark);color:var(--white);font-size:21px;text-decoration:none}
.btn-quote.hero-btn{left:52px;top:287px;width:191px;height:33px}

.intro{position:absolute;left:0;top:372px;width:786px;height:160px;background:var(--intro-bg);text-align:center}
.intro h2{margin-top:38px;font-size:19px;font-weight:400;color:var(--accent-lime)}
.intro p{font-size:11px;line-height:14px;width:600px;margin:5px auto 0}

.services{position:absolute;left:0;top:532px;width:786px;height:400px;background:var(--services-bg);text-align:center}
.services h2{margin-top:25px;font-size:19px;font-weight:400;color:var(--accent-lime)}
.service{position:absolute;top:76px;width:160px;text-align:center}
.service-photo{width:128px;height:128px;border-radius:50%;border:2px solid var(--white);margin:0 auto}
.service h3{font-size:11px;font-weight:400;margin-top:8px}
.service p{font-size:9px;line-height:11px;margin:6px auto 0;width:136px;height:44px}
.service .more{display:inline-block;margin-top:6px;font-size:8px;border:1px solid var(--white);padding:3px 5px;color:var(--white);text-decoration:none}
.view-all{position:absolute;left:328px;top:339px;width:131px;height:31px;border:1px solid var(--white);color:var(--white);font-size:11px;display:flex;align-items:center;justify-content:center;text-decoration:none}

.commercial{position:absolute;left:0;top:932px;width:786px;height:240px;background:linear-gradient(180deg,var(--soil) 0%,var(--soil-deep) 100%);text-align:center}
.commercial h2{margin-top:18px;font-size:14px;font-weight:400}
.commercial p{font-size:10px;line-height:12px;width:560px;margin:5px auto 0}
.commercial .phone{font-size:14px}
.btn-quote.cta-btn{left:236px;top:175px;width:315px;height:38px}

.footer{position:absolute;left:0;top:1172px;width:786px;height:28px;background:var(--footer);font-size:9px;display:flex;align-items:center;padding:0 52px}
.social{position:absolute;left:354px;top:5px;display:flex;gap:4px}
.social span{width:18px;height:18px;border-radius:2px}
.footer nav{margin-left:auto}
.footer nav a{color:var(--white);text-decoration:none}
</style>
</head>
<body>
<header class="hero">
  <div class="hero-scene" role="img" aria-label="Sunny lawn with blue sky, clouds and trees"></div>
  <div class="mascot" role="img" aria-label="Cartoon red lawn mower mascot"></div>
  <div class="brand"><span class="brand-dot"></span>Verdant Row</div>
  <div class="service-area">We Serve Marlow Creek &amp; Sandpiper Cove</div>
  <div class="call">Call Now: <strong>844-555-0142</strong></div>
  <nav class="nav">
    <a class="is-active" href="#">HOME</a>
    <a href="#">ABOUT US</a>
    <a href="#">OUR SERVICES</a>
    <a href="#">ESTIMATE</a>
    <a href="#">CONTACT US</a>
    <a class="portal" href="#"><svg viewBox="0 0 12 12"><circle cx="6" cy="4" r="2.5" fill="none" stroke="#fff"/><path d="M1 11c1-3 9-3 10 0" fill="none" stroke="#fff"/></svg>CLIENT PORTAL</a>
  </nav>
  <div class="tagline">
    <p>We are</p>
    <h1>Safe,<br>Reliable,<br>&amp; Responsible</h1>
  </div>
  <a class="btn-quote hero-btn" href="#">GET A QUOTE</a>
</header>

<section class="intro">
  <h2>YOUR YEAR AROUND LAWN CARE SOLUTION</h2>
  <p>Verdant Row is SAFE, Reliable, and Responsible. We make sure that all of our lawn care professionals are licensed, insured, drug-free, background checks completed and legally eligible to work.</p>
  <p>Verdant Row offers convenient online bill pay, we accepts credit cards, and we pride ourselves with a great customer service department.</p>
</section>

<section class="services">
  <h2>OUR SERVICES</h2>
  <article class="service" style="left:50px">
    <div class="service-photo" role="img" aria-label="Lawn mower cutting grass" style="background:radial-gradient(circle,#5ea832,#2f7a1a)"></div>
    <h3>Lawn Care</h3>
    <p>We welcome the opportunity to provide full maintenance service.</p>
    <a class="more" href="#">Read More</a>
  </article>
  <article class="service" style="left:227px">
    <div class="service-photo" role="img" aria-label="Pink tulips in a flower bed" style="background:radial-gradient(circle,#e07aa0,#4f8a2e)"></div>
    <h3>Flower Bed Maintenance</h3>
    <p>We are good at creating landscape designs that require minimal maintenance.</p>
    <a class="more" href="#">Read More</a>
  </article>
  <article class="service" style="left:404px">
    <div class="service-photo" role="img" aria-label="Neatly trimmed hedges" style="background:linear-gradient(180deg,#cfd6d8,#56733a 50%,#8aa058)"></div>
    <h3>Trimming and Pruning</h3>
    <p>Mowing the yard is only half the challenge.</p>
    <a class="more" href="#">Read More</a>
  </article>
  <article class="service" style="left:582px">
    <div class="service-photo" role="img" aria-label="Colourful plants and shrubs" style="background:radial-gradient(circle,#e8c04a,#6a9a38 70%)"></div>
    <h3>Plant &amp; Shrub Installation</h3>
    <p>The addition of plants and shrubs is what ties a property all together.</p>
    <a class="more" href="#">Read More</a>
  </article>
  <a class="view-all" href="#">View All Services</a>
</section>

<section class="commercial">
  <h2>Do you need property maintenance for a commercial property?</h2>
  <p>Verdant Row can establish a budget and remain within it. All costs are known. There are no hidden or indirect charges. Our safety practices, training procedures and comprehensive insurance, limit your exposure to liability as a result of careless or abusive use of equipment or chemicals.</p>
  <p>Verdant Row strives to be a one-stop 'Outdoor Service Provider'. If your outdoor services are not currently managed by one service provider let us show you the return on investment (ROI) earned by switching to Verdant Row. We solely focus on ground maintenance so you can focus on your business.</p>
  <p>Property managers love us because we make their job easy.</p>
  <p>For a refreshing lawn care experience call <span class="phone">844-555-YARD</span> today.</p>
  <a class="btn-quote cta-btn" href="#">GET A QUOTE</a>
</section>

<footer class="footer">
  <span>Copyright Verdant Row 2014. All Rights Reserved.</span>
  <div class="social">
    <span style="background:#2a9fd6"></span>
    <span style="background:#3b5998"></span>
    <span style="background:#d34836"></span>
    <span style="background:#c4302b"></span>
  </div>
  <nav><a href="#">Home</a> | <a href="#">About</a> | <a href="#">Services</a> | <a href="#">Estimate</a> | <a href="#">Contact Us</a></nav>
</footer>
</body>
</html>
```